Modern Business Card For A Digital Advertising Company

I'll be print on the Tally Prints Velvet paper http://us.tallyprints-example.com/products/velvet/business-cards.html
Need's to be modern and use the color palette of the logo or gray scales. I think integrating the pixelation of the logo in to the card and having it wrap from one side to the other could be interesting. My company provides ad operations, web development, and number of other services to websites around the world. You can see my website at http://www.brightorbitads-example.com
Contact info on the card needs to have
Dana Welby
President
p.555.308.4127
dana@brightorbitads-example.com
http://www.brightorbitads-example.com
Doesn't necessarily need to be in that order
Target Market(s)
Website owners
Industry/Entity Type
Business
Look and feel
Each slider illustrates characteristics of the customer's brand and the style your logo design should communicate.

```html
<!DOCTYPE html>
<html lang="en">
<head>
<meta charset="utf-8">
<title>Bright Orbit Ads – Business Card</title>
<link rel="stylesheet" href="https://fonts.googleapis.com/css2?family=Roboto:wght@300;400;500&display=swap">
<style>
  :root {
    --backdrop: #d9dcd9;
    --card: #ffffff;
    --green: #8cc63f;
    --green-light: #c5e39c;
    --ink: #4a4a4a;
    --ink-soft: #8a8a8a;
    --shadow: rgba(0, 0, 0, 0.18);
  }
  * { box-sizing: border-box; margin: 0; padding: 0; }
  html, body { width: 1200px; height: 900px; overflow: hidden; }
  body {
    background: var(--backdrop);
    font-family: "Roboto", Arial, sans-serif;
    color: var(--ink);
    position: relative;
  }
  .card {
    position: absolute;
    top: 296px;
    width: 540px;
    height: 309px;
    background: var(--card);
    box-shadow: 0 6px 18px var(--shadow);
    overflow: hidden;
  }
  .card--front { left: 45px; }
  .card--back { left: 615px; }

  /* pixel band that wraps from one card side to the other */
  .pixel-band {
    position: absolute;
    height: 16px;
  }
  .card--front .pixel-band {
    left: 0;
    top: 168px;
    width: 350px;
    background: linear-gradient(to right, var(--green-light), var(--green));
  }
  .card--back .pixel-band--top {
    right: 0;
    top: 96px;
    width: 290px;
    background: linear-gradient(to left, var(--green-light), var(--green));
  }

  /* logo lockup */
  .brand {
    position: absolute;
    right: 36px;
    top: 132px;
    display: flex;
    align-items: center;
    gap: 10px;
  }
  .brand__square {
    width: 38px;
    height: 38px;
    background: var(--green);
  }
  .brand__name {
    font-size: 24px;
    font-weight: 500;
    color: var(--green);
    line-height: 1;
    width: 120px;
  }

  /* back card: services */
  .services {
    position: absolute;
    right: 14px;
    top: 122px;
    display: flex;
    gap: 4px;
    list-style: none;
  }
  .service {
    width: 50px;
    display: flex;
    flex-direction: column;
    align-items: center;
    text-align: center;
    font-size: 7px;
    line-height: 1.15;
    color: var(--ink);
  }
  .service svg { width: 18px; height: 18px; margin-bottom: 3px; }
  .service--active svg { color: var(--green); }
  .service svg { color: var(--ink); }

  /* back card: identity */
  .person {
    position: absolute;
    left: 0;
    top: 196px;
    display: flex;
    align-items: flex-start;
  }
  .person .pixel-band--lead {
    position: static;
    width: 40px;
    height: 22px;
    margin-top: 4px;
    margin-right: 6px;
    background: linear-gradient(to right, var(--green-light), var(--green));
  }
  .person__name {
    font-size: 28px;
    font-weight: 300;
    letter-spacing: 1px;
    text-transform: uppercase;
    color: var(--ink);
    line-height: 1.05;
  }
  .person__title {
    font-size: 11px;
    font-weight: 400;
    color: var(--ink-soft);
  }

  .contacts {
    position: absolute;
    left: 54px;
    top: 248px;
    list-style: none;
    font-size: 13px;
    font-weight: 300;
    letter-spacing: 0.4px;
    color: var(--ink);
  }
  .contact {
    display: flex;
    align-items: center;
    gap: 10px;
    height: 17px;
  }
  .contact svg { width: 12px; height: 12px; color: var(--green); flex: none; }
</style>
</head>
<body>

<section class="card card--front" aria-label="Card front">
  <div class="pixel-band" role="img" aria-label="Green pixelated band"></div>
  <div class="brand">
    <span class="brand__square"></span>
    <span class="brand__name">Bright Orbit Ads</span>
  </div>
</section>

<section class="card card--back" aria-label="Card back">
  <div class="pixel-band pixel-band--top" role="img" aria-label="Green pixelated band"></div>

  <ul class="services">
    <li class="service service--active">
      <svg viewBox="0 0 20 20" fill="none" stroke="currentColor" stroke-width="1.6"><rect x="2" y="5" width="16" height="10" rx="1"/><circle cx="10" cy="10" r="2.5"/></svg>
      Ad Operations
    </li>
    <li class="service">
      <svg viewBox="0 0 20 20" fill="none" stroke="currentColor" stroke-width="1.8"><path d="M4 16 L14 6"/><path d="M12 4 L16 8"/><path d="M4 4 L16 16"/></svg>
      Web Development
    </li>
    <li class="service">
      <svg viewBox="0 0 20 20" fill="none" stroke="currentColor" stroke-width="1.6"><rect x="3" y="4" width="14" height="5"/><rect x="3" y="11" width="14" height="5"/></svg>
      Hosting
    </li>
    <li class="service">
      <svg viewBox="0 0 20 20" fill="none" stroke="currentColor" stroke-width="1.6"><circle cx="10" cy="10" r="7"/><path d="M10 5 V10 H14"/></svg>
      Site Speed
    </li>
    <li class="service">
      <svg viewBox="0 0 20 20" fill="none" stroke="currentColor" stroke-width="1.6"><rect x="3" y="9" width="3" height="8"/><path d="M8 9 L11 3 C13 3 13 5 12.5 8 H16 L15 17 H8 Z"/></svg>
      Social Media
    </li>
    <li class="service">
      <svg viewBox="0 0 20 20" fill="none" stroke="currentColor" stroke-width="1.8"><circle cx="8" cy="8" r="5"/><path d="M12 12 L17 17"/></svg>
      Search Engine Optimization
    </li>
  </ul>

  <div class="person">
    <div class="pixel-band pixel-band--lead" role="img" aria-label="Green pixelated accent"></div>
    <div>
      <h1 class="person__name">Dana Welby</h1>
      <p class="person__title">President</p>
    </div>
  </div>

  <ul class="contacts">
    <li class="contact">
      <svg viewBox="0 0 20 20" fill="currentColor"><path d="M5 2 L8 2 L9 6 L7 8 C8 11 9 12 12 13 L14 11 L18 12 L18 15 C18 17 16 18 14 18 C8 17 3 12 2 6 C2 4 3 2 5 2 Z"/></svg>
      555 308 4127
    </li>
    <li class="contact">
      <svg viewBox="0 0 20 20" fill="currentColor"><path d="M2 5 H18 V15 H2 Z M2 5 L10 11 L18 5" stroke="#fff" stroke-width="1.2"/></svg>
      dana@brightorbitads-example.com
    </li>
    <li class="contact">
      <svg viewBox="0 0 20 20" fill="none" stroke="currentColor" stroke-width="2.4"><circle cx="8" cy="8" r="5"/><path d="M12 12 L17 17"/></svg>
      www.brightorbitads-example.com
    </li>
  </ul>
</section>

</body>
</html>
```